Merrigal Caravan Park - Signage

We need a sign designed for our caravan & cabin park located in Karoonda in the South Australian Mallee. The sign needs to say "Merrigal Caravan Park". The park offers powered sites and self contained cabins. The sign will be displayed at the entrance to the park and will be visible from the main highway. The size of the sign will be approx.1800 wide x 1500 high. Two images that I have attached need to be displayed on the sign, but are not the prime purpose of the sign, they are just symbols that represent what other services are supplied at the park. The third image is our logo which can just be displayed along with the other two images.
I have now attached a photo of the entrance to the park where the sign will be displayed. mER
Updates

Target Market(s)

Tourism

Industry/Entity Type

Tourism

Font styles to use
Sans Serif

Requirements
Must have
• Big eye catching
Nice to have
• simple design of a caravan, design to reflect the towns reputation of being a rural farming town.
Should not have
• to much detail, the sign needs to be clear and NOT cluttered.

```html
<!DOCTYPE html>
<html lang="en">
<head>
<meta charset="utf-8">
<title>Merrigal Caravan Park – Entrance Sign</title>
<link rel="stylesheet" href="https://fonts.googleapis.com/css2?family=Marcellus+SC&family=Open+Sans:wght@700&display=swap">
<style>
  :root {
    --backdrop: #e9ebee;
    --sign-blue-light: #3550a8;
    --sign-blue: #26388f;
    --sign-blue-dark: #1b2a78;
    --sign-frame: #1a1f33;
    --strip-white: #eef0f2;
    --strip-green: #1f8a3a;
    --badge-gold: #d9b531;
    --pay-maroon: #8c1d2e;
    --service-blue: #1c5a9e;
    --ink-white: #ffffff;
  }
  * { margin: 0; padding: 0; box-sizing: border-box; }
  html, body {
    width: 1200px;
    height: 732px;
    overflow: hidden;
    background: var(--backdrop);
  }
  .canvas {
    position: relative;
    width: 1200px;
    height: 732px;
  }
  .sign {
    position: absolute;
    left: 250px;
    top: 30px;
    width: 700px;
    height: 672px;
    border: 6px solid var(--sign-frame);
    background: var(--strip-white);
    display: flex;
    flex-direction: column;
    box-shadow: 0 10px 24px rgba(0,0,0,0.18);
  }
  .sign-face {
    height: 456px;
    background: radial-gradient(ellipse at 50% 20%, var(--sign-blue-light) 0%, var(--sign-blue) 55%, var(--sign-blue-dark) 100%);
    display: flex;
    flex-direction: column;
    align-items: center;
  }
  .park-emblem {
    margin-top: 62px;
    width: 290px;
    height: 180px;
    border-radius: 10px;
    background: linear-gradient(180deg, rgba(255,255,255,0.22), rgba(255,255,255,0.10));
  }
  .park-name {
    margin-top: 40px;
    font-family: "Marcellus SC", "Times New Roman", serif;
    color: var(--ink-white);
    text-align: center;
    line-height: 1.02;
    font-size: 74px;
    letter-spacing: 1px;
    transform: rotate(-2deg);
  }
  .service-strip {
    flex: 1;
    border: 8px solid var(--strip-green);
    border-top-width: 9px;
    display: flex;
    align-items: center;
    justify-content: space-between;
    padding: 0 46px 0 40px;
  }
  .council-badge {
    width: 130px;
    height: 130px;
    border-radius: 50%;
    background: var(--badge-gold);
  }
  .payment-mark {
    display: flex;
    align-items: center;
    gap: 12px;
    background: var(--pay-maroon);
    padding: 22px 26px;
    border-radius: 8px;
  }
  .payment-mark span {
    font-family: "Open Sans", Arial, sans-serif;
    font-weight: 700;
    font-size: 34px;
    color: var(--ink-white);
  }
  .dump-point-badge {
    width: 116px;
    height: 116px;
    border-radius: 8px;
    background: var(--service-blue);
  }
</style>
</head>
<body>
  <main class="canvas">
    <section class="sign" aria-label="Merrigal Caravan Park entrance sign">
      <div class="sign-face">
        <div class="park-emblem" role="img" aria-label="Caravan beneath three pine trees emblem"></div>
        <h1 class="park-name">Merrigal<br>Caravan Park</h1>
      </div>
      <div class="service-strip">
        <div class="council-badge" role="img" aria-label="Local council badge"></div>
        <div class="payment-mark"><span>Tapcard</span></div>
        <div class="dump-point-badge" role="img" aria-label="RV dump point badge"></div>
      </div>
    </section>
  </main>
</body>
</html>
```